Webpage

I am a professional genealogist. I need a webpage that is professional looking (using the logo I chose), I can add hyperlinks and photos to if and when I want.

```html
<!DOCTYPE html>
<html lang="en">
<head>
<meta charset="utf-8">
<title>Harlow Research Services</title>
<link href="https://fonts.googleapis.com/css2?family=Roboto:wght@300;400;500&family=Open+Sans:wght@400&display=swap" rel="stylesheet">
<style>
  :root{
    --green:#80c9a6;
    --green-deep:#6dbf99;
    --green-soft:rgba(128,201,166,.85);
    --ink:#2f2f2f;
    --body:#4a4a4a;
    --muted:#777;
    --line:#e4e4e4;
    --panel:#eef1ee;
    --white:#fff;
  }
  *{box-sizing:border-box;margin:0;padding:0}
  html,body{width:851px;height:1200px;overflow:hidden;background:var(--white)}
  body{font-family:"Roboto",sans-serif;color:var(--body);position:relative}
  .page{position:relative;width:851px;height:1200px;overflow:hidden}
  .abs{position:absolute}

  .top-rule{left:0;top:0;width:851px;height:3px;background:var(--green)}
  .site-header{left:0;top:3px;width:851px;height:97px;border-bottom:1px solid var(--line)}
  .brand-mark{left:94px;top:12px;width:58px;height:58px;border-radius:50%;background:var(--green)}
  .brand-name{left:166px;top:28px;font-size:20px;font-weight:300;color:#666;line-height:20px}
  .brand-name span{display:block;padding-left:56px;font-size:16px;line-height:18px}
  .search{left:530px;top:8px;width:167px;height:21px;border:1px solid #bbb;font-size:10px;font-style:italic;color:#999;padding:4px 6px}
  .search svg{position:absolute;right:5px;top:4px}
  .social{top:8px;width:20px;height:20px;border:1px solid var(--green);border-radius:50%}
  .nav{top:58px;height:20px;font-size:12px;color:var(--ink);line-height:20px}
  .nav.active{background:var(--green);color:var(--white);padding:0 12px}

  .hero{left:0;top:100px;width:851px;height:278px;background:linear-gradient(120deg,#e9e9e9,#f4f4f4 45%,#e6e6e6)}
  .hero-photo{left:353px;top:127px;width:402px;height:228px;background:linear-gradient(135deg,#8a8a86,#5b5b57 55%,#3d3d3a)}
  .hero-title{left:40px;top:164px;width:326px;text-align:center;font-size:22px;font-weight:400;color:var(--ink)}
  .hero-text{left:60px;top:194px;width:286px;text-align:center;font-size:11.2px;line-height:18.5px;font-weight:300;color:var(--ink)}
  .btn{left:150px;top:275px;width:103px;height:31px;background:var(--green);color:var(--white);font-size:12.5px;text-align:center;line-height:31px}

  .welcome-title{left:0;top:406px;width:851px;text-align:center;font-size:20px;color:var(--ink)}
  .welcome-text{left:80px;top:438px;width:691px;text-align:center;font-size:11.2px;line-height:17.6px;font-weight:300;color:var(--ink)}

  .service-icon{width:36px;height:36px;border-radius:50%;background:var(--green)}
  .service-icon svg{display:block}
  .service-title{width:220px;text-align:center;font-size:16px;color:var(--ink);line-height:17.6px}
  .service-text{width:220px;text-align:center;font-size:11.2px;line-height:17.6px;font-weight:300;color:var(--ink)}

  .work-band{left:0;top:818px;width:851px;height:348px;background:var(--panel)}
  .section-title{font-size:17px;color:var(--ink)}
  .work-card{top:871px;width:212px;height:128px;background:var(--white);border:1px solid #ddd;box-shadow:0 1px 2px rgba(0,0,0,.08)}
  .work-image{position:absolute;left:4px;top:4px;width:202px;height:118px}
  .work-caption{position:absolute;left:4px;top:98px;width:202px;height:24px;background:var(--green-soft);color:var(--white);font-size:11px;line-height:24px;padding-left:7px;white-space:nowrap;overflow:hidden;font-weight:300}
  .about-text{left:90px;top:1063px;width:420px;font-size:11.2px;line-height:17.6px;font-weight:300;color:var(--ink)}
  .contact-text{left:538px;top:1063px;width:230px;font-size:11.2px;line-height:17.6px;font-weight:300;color:var(--ink)}
  .contact-text b{font-weight:500}

  .site-footer{left:0;top:1166px;width:851px;height:34px;background:var(--green);font-family:"Open Sans",sans-serif;font-size:10px;color:var(--white)}
  .footer-links{position:absolute;left:94px;top:10px;word-spacing:2px}
  .footer-links i{font-style:normal;padding:0 7px}
  .copyright{position:absolute;right:98px;top:10px}
</style>
</head>
<body>
<div class="page">
  <div class="abs top-rule"></div>
  <header class="abs site-header">
    <div class="abs brand-mark"></div>
    <div class="abs brand-name">Harlow Research<span>Services</span></div>
    <div class="abs search">search...
      <svg width="11" height="11" viewBox="0 0 11 11"><circle cx="4.5" cy="4.5" r="3.3" fill="none" stroke="#80c9a6" stroke-width="1.5"/><line x1="7" y1="7" x2="10" y2="10" stroke="#80c9a6" stroke-width="1.8"/></svg>
    </div>
    <div class="abs social" style="left:711px"></div>
    <div class="abs social" style="left:736px"></div>
    <nav>
      <a class="abs nav active" style="left:397px">Home</a>
      <a class="abs nav" style="left:463px">About</a>
      <a class="abs nav" style="left:516px">Services</a>
      <a class="abs nav" style="left:582px">Publications</a>
      <a class="abs nav" style="left:667px">Blog</a>
      <a class="abs nav" style="left:714px">Contact</a>
    </nav>
  </header>

  <section class="abs hero" role="img" aria-label="Faded background of old family photographs and a pocket watch"></section>
  <div class="abs hero-photo" role="img" aria-label="Vintage black and white photograph of a family seated outdoors by a wooden fence"></div>
  <h1 class="abs hero-title">Kinship Determination</h1>
  <p class="abs hero-text">Sed ut perspiciatis unde omnis iste atus error sit voluptatem accusantium doloque laudarat tium, totam rem aperiam, eaque ipsa quae .</p>
  <a class="abs btn">Learn More</a>

  <h2 class="abs welcome-title">Welcome to Harlow Research Services (HRS)</h2>
  <p class="abs welcome-text">Sed ut perspiciatis unde omnis iste natus error sit voluptatem accusantium doloremque laudantium, totam rem aperiam, eaque tas sit<br>aspernatur aut odit aut fugit, sed quia consequuntur magni dolores eos qui ratione voluptatem sequi nesciunt.</p>

  <!-- services row 1 -->
  <div class="abs service-icon" style="left:176px;top:492px"><svg width="36" height="36"><path d="M12 26 C20 22,16 14,24 10 M12 10 C20 14,16 22,24 26" stroke="#fff" stroke-width="2" fill="none"/></svg></div>
  <h3 class="abs service-title" style="left:86px;top:543px">Forensic Genealogy</h3>
  <p class="abs service-text" style="left:86px;top:572px">Sed ut perspiciatis unde omnis iste natus error sit voluptatem accusantium dolorem que laudantium totam rem aperiam.</p>

  <div class="abs service-icon" style="left:402px;top:492px"><svg width="36" height="36"><rect x="15" y="8" width="6" height="6" fill="#fff"/><path d="M18 14v4M10 18h16M10 18v4M18 18v4M26 18v4" stroke="#fff" stroke-width="1.5"/><rect x="7" y="22" width="6" height="6" fill="#fff"/><rect x="15" y="22" width="6" height="6" fill="#fff"/><rect x="23" y="22" width="6" height="6" fill="#fff"/></svg></div>
  <h3 class="abs service-title" style="left:312px;top:543px">Kinship Determination</h3>
  <p class="abs service-text" style="left:312px;top:572px">Sed ut perspiciatis unde omnis iste natus error sit voluptatem accusantium dolorem que laudantium totam rem aperiam.</p>

  <div class="abs service-icon" style="left:628px;top:492px"><svg width="36" height="36"><circle cx="16" cy="16" r="7" stroke="#fff" stroke-width="2.2" fill="none"/><line x1="21" y1="21" x2="27" y2="27" stroke="#fff" stroke-width="3"/></svg></div>
  <h3 class="abs service-title" style="left:541px;top:535px">Research Analysis<br>and&nbsp; Consultation</h3>
  <p class="abs service-text" style="left:541px;top:572px">Sed ut perspiciatis unde omnis iste natus error sit voluptatem accusantium dolorem que laudantium totam rem aperiam.</p>

  <!-- services row 2 -->
  <div class="abs service-icon" style="left:176px;top:652px"><svg width="36" height="36"><path d="M18 8a6 6 0 0 1 6 6c0 5-6 12-6 12s-6-7-6-12a6 6 0 0 1 6-6z" fill="#fff"/><circle cx="18" cy="14" r="2.2" fill="#80c9a6"/></svg></div>
  <h3 class="abs service-title" style="left:86px;top:706px">Texas Researcher</h3>
  <p class="abs service-text" style="left:86px;top:732px">Sed ut perspiciatis unde omnis iste natus error sit voluptatem accusantium dolorem que laudantium totam rem aperiam.</p>

  <div class="abs service-icon" style="left:402px;top:652px"><svg width="36" height="36"><rect x="11" y="8" width="14" height="19" fill="#fff"/><path d="M14 13h8M14 17h8M14 21h5" stroke="#80c9a6" stroke-width="1.5"/></svg></div>
  <h3 class="abs service-title" style="left:312px;top:706px">Texas Researcher</h3>
  <p class="abs service-text" style="left:312px;top:732px">Sed ut perspiciatis unde omnis iste natus error sit voluptatem accusantium dolorem que laudantium totam rem aperiam.</p>

  <div class="abs service-icon" style="left:630px;top:652px"><svg width="36" height="36"><circle cx="18" cy="18" r="10" stroke="#fff" stroke-width="1.8" fill="none"/><path d="M18 12v12M12 18h12" stroke="#fff" stroke-width="3"/></svg></div>
  <h3 class="abs service-title" style="left:541px;top:706px">More Services</h3>
  <p class="abs service-text" style="left:541px;top:732px">Sed ut perspiciatis unde omnis iste natus error sit voluptatem accusantium dolorem que laudantium totam rem aperiam.</p>

  <section class="abs work-band"></section>
  <h2 class="abs section-title" style="left:90px;top:837px">Latest Work</h2>
  <div class="abs work-card" style="left:90px">
    <div class="work-image" role="img" aria-label="Scientist examining a sample through a microscope in a lab" style="background:linear-gradient(135deg,#d8dde2,#8e9aa6 60%,#5d6a78)"></div>
    <div class="work-caption">DNA Testing in Crime Lab</div>
  </div>
  <div class="abs work-card" style="left:318px">
    <div class="work-image" role="img" aria-label="Sepia portrait of a family standing together" style="background:linear-gradient(135deg,#c9b9a3,#8a7660 55%,#5b4a3a)"></div>
    <div class="work-caption">Kinship Determination with the Smith</div>
  </div>
  <div class="abs work-card" style="left:545px">
    <div class="work-image" role="img" aria-label="Old photographs with a pocket watch" style="background:linear-gradient(135deg,#d9b896,#a97e58 55%,#6e4f34)"></div>
    <div class="work-caption">Lorem Ipsum Dolor</div>
  </div>

  <h2 class="abs section-title" style="left:90px;top:1030px">About Us</h2>
  <p class="abs about-text">Sed ut perspiciatis unde omnis iste natus error sit voluptatem accusantium dolo-<br>remque laudantium, totam rem aperiam, eaque tas sit aspernatur aut odit aut fugit,<br>sed quia consequuntur magni dolores eos qui ratione voluptatem sequi nesciunt.<br>Neque porro quisquam est, qui dolorem ipsum quia doadip.</p>

  <h2 class="abs section-title" style="left:538px;top:1030px;font-weight:500">Contact</h2>
  <p class="abs contact-text"><b>Dana Harlow,</b> Professional Genealogist<br><b>address:</b> PO Box 4821 Austin, TX<br><b>phone:</b> 555-210-4821&nbsp;&nbsp;&nbsp;&nbsp; <b>cel:</b> 555-318-2097<br><b>email:</b> dharlow@example.net</p>

  <footer class="abs site-footer">
    <div class="footer-links">Home<i>|</i>About<i>|</i>Services<i>|</i>Publications<i>|</i>Blog<i>|</i>Contact</div>
    <div class="copyright">© 2014 HRS. All Right Reserved</div>
  </footer>
</div>
</body>
</html>
```